Digital ad to Parent Funnel

Those Puddle Jumpers works with preschoolers (also ages 2-8) doing hands-on activities that are Science Tech Engineering and Math (STEM) as a service business. The design is subtly colorful with the attached swatch definitions. Hexagons are a theme on the website.
www.thosepuddlejumpers.com
The purpose is on social media with a call to action to a landing page. I'd like placeholder text so I can be the copywriter. The banner I see is vertical, longer than wider. Design elements are welcoming, cheerful, and concrete. Pictures included are thematic for reference
https://www.pinterest.com/puddlejumpersKV/website-mood-board/
I'd like fonts that are more used than Dosis, which has a child-like font but doesn't render well online. Versatile design desired for deferring ad sizes, if possible. My laptop has InDesign.
Thanks!

```html
<!DOCTYPE html>
<html lang="en">
<head>
<meta charset="utf-8">
<title>Those Puddle Jumpers – Vertical Ad</title>
<link rel="stylesheet" href="https://fonts.googleapis.com/css2?family=Delius&display=swap">
<style>
  :root {
    --bg: #e9e0d6;
    --purple: #5b2d91;
    --ink: #1d1a1a;
    --magenta: #e5178f;
    --lime: #d6ea3a;
    --red: #f0321e;
    --orange: #f7941d;
    --violet: #6b3fd6;
    --blue: #4b3fc9;
    --teal: #19d3c5;
    --lilac: #b36ae8;
  }
  html, body {
    margin: 0;
    padding: 0;
    width: 1200px;
    height: 3219px;
    overflow: hidden;
    background: var(--bg);
  }
  .ad {
    position: relative;
    width: 1200px;
    height: 3219px;
    background: var(--bg);
    font-family: "Delius", "Comic Sans MS", cursive;
    overflow: hidden;
  }
  .ad__art {
    position: absolute;
    inset: 0;
    width: 1200px;
    height: 3219px;
  }
  .ad__title {
    position: absolute;
    left: 0;
    top: 1500px;
    width: 1200px;
    margin: 0;
    text-align: center;
    padding-right: 40px;
    box-sizing: border-box;
    font-size: 165px;
    font-weight: 400;
    line-height: 1;
    color: var(--purple);
    letter-spacing: -2px;
  }
  .ad__subtitle {
    position: absolute;
    left: 640px;
    top: 1715px;
    margin: 0;
    font-size: 86px;
    font-weight: 400;
    line-height: 1;
    color: var(--ink);
    transform: translateX(-50%);
    white-space: nowrap;
    margin-left: 50px;
  }
  .ad__body {
    position: absolute;
    left: 110px;
    top: 1860px;
    width: 1000px;
    margin: 0;
    text-align: center;
    font-size: 44px;
    line-height: 82px;
    color: var(--ink);
  }
  .ad__brand {
    position: absolute;
    left: 300px;
    top: 2520px;
    width: 600px;
    text-align: center;
    font-size: 84px;
    line-height: 1.05;
    color: var(--purple);
  }
</style>
</head>
<body>
<main class="ad">
  <svg class="ad__art" viewBox="0 0 1200 3219" xmlns="http://www.w3.org/2000/svg">
    <defs>
      <clipPath id="photo-clip">
        <polygon points="698,213 1157,478 1157,1008 698,1273 239,1008 239,478"/>
      </clipPath>
      <linearGradient id="photo-tones" x1="0" y1="0" x2="1" y2="1">
        <stop offset="0" stop-color="#f4eef4"/>
        <stop offset="0.45" stop-color="#d9b9d6"/>
        <stop offset="0.75" stop-color="#8a6f8e"/>
        <stop offset="1" stop-color="#1f2240"/>
      </linearGradient>
      <polygon id="hex" points="0,-1 0.866,-0.5 0.866,0.5 0,1 -0.866,0.5 -0.866,-0.5"/>
      <polygon id="hex-top" points="0,-1 0.866,-0.5 0,0 -0.866,-0.5"/>
    </defs>

    <g class="photo-frame">
      <rect x="239" y="213" width="918" height="1060" fill="url(#photo-tones)"
            clip-path="url(#photo-clip)" role="img"
            aria-label="Photo: a smiling young child holding up a colourful pinwheel"/>
      <polygon points="698,213 1157,478 1157,1008 698,1273 239,1008 239,478"
               fill="none" stroke="var(--purple)" stroke-width="16" stroke-linejoin="miter"/>
    </g>

    <g class="cubes cubes--top-left" opacity="0.9">
      <g transform="translate(190 200) scale(78)"><use href="#hex" fill="var(--magenta)"/><use href="#hex-top" fill="#fff" opacity="0.2"/></g>
      <g transform="translate(190 365) scale(78)"><use href="#hex" fill="var(--red)"/><use href="#hex-top" fill="#fff" opacity="0.2"/></g>
      <g transform="translate(350 245) scale(86)"><use href="#hex" fill="var(--lime)"/><use href="#hex-top" fill="#fff" opacity="0.25"/></g>
    </g>

    <g class="cubes cubes--photo-corner" opacity="0.9">
      <g transform="translate(840 1195) scale(96)"><use href="#hex" fill="var(--violet)"/><use href="#hex-top" fill="#fff" opacity="0.2"/></g>
      <g transform="translate(1015 1195) scale(96)"><use href="#hex" fill="var(--blue)"/><use href="#hex-top" fill="#fff" opacity="0.2"/></g>
      <g transform="translate(925 1365) scale(96)"><use href="#hex" fill="var(--teal)"/><use href="#hex-top" fill="#fff" opacity="0.2"/></g>
    </g>

    <g class="cubes cubes--bottom-left" opacity="0.92">
      <g transform="translate(270 2935) scale(105)"><use href="#hex" fill="var(--orange)"/><use href="#hex-top" fill="#fff" opacity="0.25"/></g>
      <g transform="translate(80 3090) scale(170)"><use href="#hex" fill="var(--red)"/><use href="#hex-top" fill="#fff" opacity="0.15"/></g>
      <g transform="translate(265 3125) scale(70)"><use href="#hex" fill="var(--lime)"/><use href="#hex-top" fill="#fff" opacity="0.25"/></g>
    </g>

    <g class="cubes cubes--bottom-right" opacity="0.92">
      <g transform="translate(925 2905) scale(80)"><use href="#hex" fill="var(--magenta)"/><use href="#hex-top" fill="#fff" opacity="0.2"/></g>
      <g transform="translate(1070 2845) scale(72)"><use href="#hex" fill="var(--lilac)"/><use href="#hex-top" fill="#fff" opacity="0.2"/></g>
      <g transform="translate(1110 3125) scale(175)"><use href="#hex" fill="var(--blue)"/><use href="#hex-top" fill="#fff" opacity="0.15"/></g>
    </g>
  </svg>

  <h1 class="ad__title">Lorem Ipsum</h1>
  <p class="ad__subtitle">is simply dummy</p>
  <p class="ad__body">Lorem Ipsum is simply dummy text of the printing and typesetting industry. Lorem Ipsum has been the industry's standard dummy text ever since the 1500s, when an unknown printer took a galley of type and scrambled it to make a type specimen book.</p>

  <div class="ad__brand">Those Puddle Jumpers</div>
</main>
</body>
</html>
```